Vehicles Brochure Diagram

Task Outline
Create diagrams for our new vehicles brochures

Task Description

Who are we:
TLR is New Zealand's largest Business Group Buying organisation, helping organisations nationwide reduce their running costs. We offer members the best deals from over 100 Contracted Suppliers, anything from vehicles, stationery to electronics and coffee.

The project:
We need 2 diagrams to illustrate the benefits of our vehicle services. The diagram will be used in our brochures (example attached)

1. A Diagram illustrating/explaining the elements that are involved in purchasing a new car & how our service ties it all together to provide the best solution.
- Please see the Diagram 1 PDF for a rough wireframe of the elements involved

2. Another small diagram inserted on an separate page to demonstrate how our services can increase safety & profit and reduce costs & risks (PDF: Diagram 2 Details)

The design needs to be clean, clear and simple that it’s easy to understand within a few seconds of looking at it. Feel free to explore with different elements in the realm of infographics, flowcharts & diagrams to best communicate the idea visually.
Updates

Just thought I’ll share some of the feedback we’re giving tosubmissions that have been coming through to help with new submissions

-Challenge & be creative about the ways you demonstratethe elements

-We don’t want to see your design replicating the ones that isdrawn. The purpose of it is only to provide you with the content in context

-We can’t emphasis enough that the style pdf is only areference and not the look you should imitate. 

If you have any question please feel free to contact me.Looking forward to see your designs!

Reason: We're keen to see more approaches & creative ways of interpreting the content rather than a standard cycle diagram. Entries so far have been good but quite literal, we will provide feedback to help steer it in the right direction.

Target Market(s)

Business professionals, Decision makers on a corporate level & prospects.

Industry/Entity Type

Electronics

Requirements
Must have

• Likes – simple, clean & clear, uncluttered

Dislikes – Overcrowded images, text, & colours. Overly expressive typeface. Please no literal illustration of our sketches or colored version of our sketch.

Font: -Myriad Pro

Colour: Please refer to the color palette in the ‘Diagram Color & Style’ PDF

The brochures are attached with content to provide context that might inform the design better,

Dimensions & the amount of space you have to work with will also be highlighted

```html
<!DOCTYPE html>
<html lang="en">
<head>
<meta charset="utf-8">
<title>Vehicle Purchase Diagram</title>
<link rel="stylesheet" href="https://fonts.googleapis.com/css2?family=Arimo:wght@400;700&display=swap">
<style>
  :root {
    --bg: #ffffff;
    --ink: #000000;
    --label: #ffffff;
    --green-light: #5ea64e;
    --green-dark: #1d6a35;
    --green-edge: #2f8a3e;
    --sky-light: #8fd3f8;
    --sky-mid: #4db6e6;
    --sky-pale: #bfe5f5;
    --navy: #0f4c8f;
    --ring-dark: #1e5fa6;
  }
  html, body {
    margin: 0;
    padding: 0;
    width: 1200px;
    height: 986px;
    overflow: hidden;
    background: var(--bg);
  }
  .canvas {
    position: relative;
    width: 1200px;
    height: 986px;
    font-family: "Arimo", Arial, sans-serif;
  }
  .headline {
    position: absolute;
    left: 72px;
    top: 56px;
    margin: 0;
    font-size: 37px;
    font-weight: 700;
    color: var(--ink);
    letter-spacing: 0.2px;
  }
  .diagram {
    position: absolute;
    left: 0;
    top: 0;
  }
  .box-title { font-weight: 700; font-size: 27px; fill: var(--label); }
  .box-item { font-weight: 400; font-size: 23px; fill: var(--label); }
  .hub-title { font-weight: 700; font-size: 47px; fill: var(--label); }
</style>
</head>
<body>
<div class="canvas">
  <h1 class="headline">There is more to a vehicle purchase than just the price</h1>

  <svg class="diagram" width="1200" height="986" viewBox="0 0 1200 986" xmlns="http://www.w3.org/2000/svg">
    <defs>
      <radialGradient id="hubFill" cx="0.3" cy="0.25" r="0.9">
        <stop offset="0" stop-color="var(--sky-mid)"/>
        <stop offset="0.5" stop-color="#6cc3ea"/>
        <stop offset="1" stop-color="var(--sky-pale)"/>
      </radialGradient>
      <linearGradient id="cardFill" x1="0" y1="0" x2="1" y2="1">
        <stop offset="0" stop-color="var(--green-light)"/>
        <stop offset="1" stop-color="var(--green-dark)"/>
      </linearGradient>
      <linearGradient id="ringTop" gradientUnits="userSpaceOnUse" x1="340" y1="0" x2="760" y2="0">
        <stop offset="0" stop-color="var(--sky-light)"/>
        <stop offset="1" stop-color="var(--ring-dark)"/>
      </linearGradient>
      <linearGradient id="ringRight" gradientUnits="userSpaceOnUse" x1="0" y1="780" x2="0" y2="420">
        <stop offset="0" stop-color="var(--sky-light)"/>
        <stop offset="1" stop-color="var(--ring-dark)"/>
      </linearGradient>
      <linearGradient id="ringBottom" gradientUnits="userSpaceOnUse" x1="380" y1="0" x2="760" y2="0">
        <stop offset="0" stop-color="var(--ring-dark)"/>
        <stop offset="0.5" stop-color="var(--sky-light)"/>
        <stop offset="1" stop-color="var(--ring-dark)"/>
      </linearGradient>
      <linearGradient id="ringLeft" gradientUnits="userSpaceOnUse" x1="0" y1="410" x2="0" y2="730">
        <stop offset="0" stop-color="var(--ring-dark)"/>
        <stop offset="0.5" stop-color="var(--sky-light)"/>
        <stop offset="1" stop-color="var(--ring-dark)"/>
      </linearGradient>
    </defs>

    <!-- ring segments -->
    <g class="ring" fill="none" stroke-width="60">
      <path d="M 332 431 A 275 275 0 0 1 781 391" stroke="url(#ringTop)"/>
      <path d="M 781 745 A 275 275 0 0 0 819 452" stroke="url(#ringRight)"/>
      <path d="M 359 745 A 275 275 0 0 0 747 779" stroke="url(#ringBottom)"/>
      <path d="M 332 431 A 275 275 0 0 0 332 705" stroke="url(#ringLeft)"/>
    </g>

    <!-- hub -->
    <circle class="hub" cx="570" cy="568" r="245" fill="url(#hubFill)"/>
    <text class="hub-title" x="560" y="470" text-anchor="middle">Best fit for</text>
    <text class="hub-title" x="560" y="516" text-anchor="middle">Purpose</text>

    <g class="car-icon" fill="var(--label)">
      <path d="M500 575 L516 537 Q520 530 530 530 L604 530 Q614 530 618 537 L634 575 Z M508 568 L626 568 L612 540 Q609 536 602 536 L532 536 Q525 536 522 540 Z" fill-rule="evenodd"/>
      <rect x="477" y="570" width="180" height="82" rx="22"/>
      <rect x="476" y="566" width="26" height="16" rx="8"/>
      <rect x="632" y="566" width="26" height="16" rx="8"/>
      <rect x="484" y="640" width="26" height="30" rx="6"/>
      <rect x="626" y="640" width="26" height="30" rx="6"/>
      <circle cx="512" cy="612" r="8" fill="#7cc8ec"/>
      <circle cx="620" cy="612" r="8" fill="#7cc8ec"/>
      <rect x="508" y="630" width="120" height="8" rx="4" fill="#7cc8ec"/>
    </g>

    <!-- cards -->
    <g class="card card-disposal">
      <rect x="81" y="219" width="330" height="201" rx="16" fill="url(#cardFill)" stroke="var(--green-edge)" stroke-width="3"/>
      <path d="M83 232 Q83 221 96 221 L396 221 Q409 221 409 232 L409 282 Q250 300 83 318 Z" fill="#ffffff" opacity="0.16"/>
      <text class="box-title" x="97" y="261">End of Life</text>
      <text class="box-title" x="97" y="297">Disposal</text>
    </g>

    <g class="card card-run">
      <rect x="720" y="217" width="330" height="202" rx="16" fill="url(#cardFill)" stroke="var(--green-edge)" stroke-width="3"/>
      <path d="M722 230 Q722 219 735 219 L1035 219 Q1048 219 1048 230 L1048 268 Q900 285 722 300 Z" fill="#ffffff" opacity="0.16"/>
      <text class="box-title" x="1018" y="262" text-anchor="end">Cost to Run</text>
      <text class="box-item" x="1018" y="302" text-anchor="end">Fuel</text>
      <text class="box-item" x="1018" y="331" text-anchor="end">Tyres</text>
      <text class="box-item" x="1018" y="361" text-anchor="end">Rego</text>
      <text class="box-item" x="1018" y="390" text-anchor="end">RoC</text>
    </g>

    <g class="card card-manage">
      <rect x="714" y="707" width="330" height="203" rx="16" fill="url(#cardFill)" stroke="var(--green-edge)" stroke-width="3"/>
      <path d="M716 720 Q716 709 729 709 L1029 709 Q1042 709 1042 720 L1042 770 Q880 784 716 798 Z" fill="#ffffff" opacity="0.16"/>
      <text class="box-title" x="1018" y="753" text-anchor="end">Cost to Manage</text>
      <text class="box-item" x="1018" y="801" text-anchor="end">Lease</text>
      <text class="box-item" x="1018" y="831" text-anchor="end">Finance Tax</text>
      <text class="box-item" x="1018" y="861" text-anchor="end">Insurance</text>
    </g>

    <g class="card card-company">
      <rect x="77" y="711" width="330" height="203" rx="16" fill="url(#cardFill)" stroke="var(--green-edge)" stroke-width="3"/>
      <path d="M79 724 Q79 713 92 713 L392 713 Q405 713 405 724 L405 756 Q240 775 79 795 Z" fill="#ffffff" opacity="0.16"/>
      <text class="box-title" x="88" y="750">Company</text>
      <text class="box-title" x="88" y="777">Requirements</text>
      <text class="box-item" x="88" y="820">Safety</text>
      <text class="box-item" x="90" y="849">Sustainability</text>
      <text class="box-item" x="90" y="878">Specifications</text>
    </g>

    <!-- arrowheads -->
    <g class="arrowheads" fill="var(--navy)">
      <polygon points="690,386 728,297 755,356"/>
      <polygon points="748,433 793,375 856,420"/>
      <polygon points="683,745 751,782 716,848"/>
      <polygon points="421,743 366,788 405,852"/>
      <polygon points="277,713 384,686 344,746"/>
      <polygon points="286,408 364,385 393,460"/>
    </g>
  </svg>
</div>
</body>
</html>
```